Tallbridge needs a new rocket based website

We need a new website that will be based on our rocket ship logo. We develop innovative solutions for enterprises. We would like to see a design that when the pages scroll, the rocket launches and goes from launch through a journey, similar to how we approach our customer. We would like areas for "Who are we", "What can we do", "What have we done", "How can we help". http://www.tallbridge.com.au is our current website

Target Market(s)

Government, Enterprise, Cloud

Industry/Entity Type

Software Service

Coding

Coded - Design and coding required

Number of Pages Required

2 page

Requirements
Must have
• We would like to see a design that when the pages scroll, the rocket launches and goes from launch through a journey, similar to how we approach our customer.
• Must have a home page and a detail page.
• Would like to see the logo/rocket animate in some way when you scroll through he page.

```html
<!DOCTYPE html>
<html lang="en">
<head>
<meta charset="utf-8">
<title>Tallbridge</title>
<link rel="stylesheet" href="https://fonts.googleapis.com/css2?family=Montserrat:wght@400;500;600;700&family=Open+Sans:wght@400;600&display=swap">
<style>
:root{
  --orange:#f7941d;
  --orange-deep:#e8800c;
  --orange-light:#fbb040;
  --charcoal:#3a3a3c;
  --charcoal-deep:#2c2d30;
  --text:#4a4a4a;
  --muted:#6d6d6d;
  --field:#efefef;
  --white:#ffffff;
}
*{box-sizing:border-box;margin:0;padding:0}
html,body{width:1200px;height:4852px;overflow:hidden}
body{position:relative;background:var(--white);font-family:"Open Sans",Arial,sans-serif;color:var(--text)}
.abs{position:absolute}

/* hero */
.hero{left:0;top:0;width:1200px;height:1100px}
.hero-bg{position:absolute;inset:0}
.brand{left:39px;top:52px;font-family:"Montserrat",Arial,sans-serif;font-weight:700;font-size:40px;color:var(--white);display:flex;align-items:center;gap:12px}
.brand-dot{width:18px;height:18px;border-radius:50%;background:var(--white)}
.main-nav{right:40px;top:62px;display:flex;gap:40px;font-family:"Montserrat",Arial,sans-serif;font-weight:500;font-size:17px;color:var(--white)}
.rocket-art{left:150px;top:90px;width:440px;height:950px;border-radius:50%;
  background:radial-gradient(ellipse at 50% 45%,rgba(255,255,255,.75) 0%,rgba(255,230,190,.5) 30%,rgba(247,148,29,0) 68%)}
.hero-title{left:556px;top:308px;width:540px;font-family:"Montserrat",Arial,sans-serif;font-weight:700;font-size:36px;line-height:48px;color:var(--white)}
.hero-sub{left:556px;top:540px;width:520px;font-family:"Montserrat",Arial,sans-serif;font-size:23px;line-height:34px;color:var(--white)}
.btn-outline{left:556px;top:653px;width:285px;height:56px;border:3px solid var(--white);border-radius:30px;color:var(--white);font-family:"Montserrat",Arial,sans-serif;font-weight:700;font-size:23px;display:flex;align-items:center;justify-content:center}

/* section headings */
.section-title{left:0;width:1200px;text-align:center;font-family:"Montserrat",Arial,sans-serif;font-weight:600;font-size:32px;color:var(--charcoal);display:flex;justify-content:center;align-items:center;gap:14px}
.section-title .accent{color:var(--orange)}
.section-title .mark{width:14px;height:14px;border-radius:50%;background:var(--orange)}
.section-title.light{color:var(--white)}

/* services */
.service-photo{width:318px;height:314px;border-radius:22px;border:8px solid var(--white);box-shadow:0 4px 18px rgba(0,0,0,.25)}
.photo-tech{background:linear-gradient(135deg,#5a4120,#c08a3a 45%,#3a2a16)}
.photo-cloud{background:linear-gradient(135deg,#1f2a10,#6f7a1c 50%,#2a3212)}
.photo-meeting{background:linear-gradient(135deg,#d9dde2,#7c8794 55%,#3b4047)}
.photo-dev{background:linear-gradient(135deg,#2a1d0e,#a06a2a 50%,#3a2712)}
.service-title{font-family:"Montserrat",Arial,sans-serif;font-weight:500;font-size:32px;color:var(--orange)}
.service-text{font-family:"Montserrat",Arial,sans-serif;font-size:21px;line-height:32px;color:var(--muted);width:400px;margin-top:14px}

/* work */
.work-band{left:0;top:2678px;width:1200px;height:730px}
.work-card{top:2878px;width:313px;height:324px;background:#f2f2f2;border-radius:8px;padding:24px 22px}
.work-card h3{font-family:"Montserrat",Arial,sans-serif;font-weight:500;font-size:14px;text-transform:uppercase;color:#222;display:flex;align-items:center;gap:8px;height:34px}
.work-card .seal{width:26px;height:26px;border-radius:50%;background:#9a9a9a}
.work-card p{margin-top:26px;font-size:17px;line-height:22px;color:#333}
.arrow-btn{top:3012px;width:56px;height:56px;border-radius:50%;background:var(--orange);display:flex;align-items:center;justify-content:center}

/* contact form */
.field{height:50px;background:var(--field);font-family:"Montserrat",Arial,sans-serif;font-size:15px;color:#333;padding:16px 12px}
.btn-solid{left:479px;top:3810px;width:240px;height:48px;border-radius:26px;background:var(--orange);color:var(--white);font-family:"Montserrat",Arial,sans-serif;font-weight:600;font-size:21px;display:flex;align-items:center;justify-content:center}

/* map + footer */
.map-area{left:0;top:3946px;width:1200px;height:360px;background:linear-gradient(180deg,#e9e6df,#dcd8cf)}
.footer-bg{left:0;top:4180px;width:1200px;height:630px}
.footer-brand{left:0;top:4430px;width:1200px;text-align:center;font-family:"Montserrat",Arial,sans-serif;font-weight:700;font-size:40px;color:var(--white);display:flex;justify-content:center;align-items:center;gap:12px}
.footer-col{top:4545px;font-family:"Montserrat",Arial,sans-serif;color:var(--white)}
.footer-col h4{font-size:15px;font-weight:700;padding-bottom:10px;border-bottom:1px solid rgba(255,255,255,.5);width:200px}
.footer-col ul{list-style:none;margin-top:14px}
.footer-col li{font-size:14px;line-height:22px;display:flex;align-items:center;gap:10px}
.tri{width:0;height:0;border-left:7px solid var(--white);border-top:5px solid transparent;border-bottom:5px solid transparent}
.icon-ring{width:20px;height:20px;border-radius:50%;border:2px solid var(--orange);flex:none}
.newsletter p{font-size:14px;line-height:20px;margin-top:14px;width:280px}
.email-field{margin-top:10px;width:260px;height:32px;border-radius:16px;background:var(--white);color:#333;font-size:13px;padding:8px 16px}
.subscribe{margin-top:12px;width:140px;height:28px;border-radius:14px;background:var(--orange);font-size:12px;font-weight:700;display:flex;align-items:center;justify-content:center}
.bottom-bar{left:0;top:4809px;width:1200px;height:43px;background:var(--orange);display:flex;align-items:center;justify-content:space-between;padding:0 20px;font-family:"Montserrat",Arial,sans-serif;font-size:12px;font-weight:600;color:var(--white)}
.socials{display:flex;gap:10px}
.socials span{width:18px;height:18px;border-radius:50%;background:var(--white)}
</style>
</head>
<body>

<header class="abs hero">
  <svg class="hero-bg" width="1200" height="1100" viewBox="0 0 1200 1100">
    <defs>
      <linearGradient id="heroFill" x1="0" y1="0" x2="0" y2="1">
        <stop offset="0" stop-color="#f39a22"/>
        <stop offset="1" stop-color="#eb870f"/>
      </linearGradient>
    </defs>
    <polygon points="0,0 1200,0 1200,960 600,1085 0,960" fill="#d9770a"/>
    <polygon points="0,0 1200,0 1200,940 600,1062 0,940" fill="url(#heroFill)"/>
    <path d="M0,1000 Q150,930 300,985 Q450,930 600,990 Q750,930 900,985 Q1050,930 1200,990 L1200,1100 L0,1100Z" fill="#ffffff"/>
    <polygon points="0,990 600,1070 1200,990 1200,1000 600,1082 0,1000" fill="#e8800c"/>
  </svg>
  <div class="abs brand"><span class="brand-dot"></span>Tallbridge</div>
  <nav class="abs main-nav"><span>Who Are We</span><span>What Can We Do</span><span>What Have We Done</span><span>How Can We Help</span></nav>
  <div class="abs rocket-art" role="img" aria-label="Illustration of the rocket launching upward on a column of glowing smoke"></div>
  <h1 class="abs hero-title">Offering the latest in<br>enterprise architecture,<br>design and development<br>of bespoke software solutions</h1>
  <p class="abs hero-sub">Always researching and implementing<br>the latest technology for customers.</p>
  <div class="abs btn-outline">Get Started</div>
</header>

<h2 class="abs section-title" style="top:1196px"><span class="mark"></span><span>What <span class="accent">Can We Do</span></span></h2>

<section>
  <div class="abs service-photo photo-tech" style="left:139px;top:1294px" role="img" aria-label="Photo of a glowing digital circuit display"></div>
  <div class="abs" style="left:508px;top:1392px"><h3 class="service-title">e-Parliament</h3><p class="service-text">All of your Parliamentary software and business process needs.</p></div>

  <div class="abs" style="left:356px;top:1716px"><h3 class="service-title">Cloud</h3><p class="service-text">Nimbus Suite, Migration,<br>Security, Customisations.</p></div>
  <div class="abs service-photo photo-cloud" style="left:744px;top:1617px" role="img" aria-label="Photo of a hand touching cloud computing icons"></div>

  <div class="abs service-photo photo-meeting" style="left:139px;top:1940px" role="img" aria-label="Photo of business people reviewing charts on a tablet"></div>
  <div class="abs" style="left:508px;top:2038px"><h3 class="service-title">Architecture &amp; Design</h3><p class="service-text">Business process design, technology strategy and architecture.</p></div>

  <div class="abs" style="left:327px;top:2362px"><h3 class="service-title">Software Development</h3><p class="service-text">Software development including business apps, web and mobile.</p></div>
  <div class="abs service-photo photo-dev" style="left:744px;top:2266px" role="img" aria-label="Photo of hands typing on a laptop with code overlay"></div>
</section>

<section>
  <svg class="abs work-band" width="1200" height="730" viewBox="0 0 1200 730" role="img" aria-label="Dark background photo of a person using a tablet">
    <defs>
      <linearGradient id="workFill" x1="0" y1="0" x2="1" y2="1">
        <stop offset="0" stop-color="#3f4044"/>
        <stop offset=".5" stop-color="#55575c"/>
        <stop offset="1" stop-color="#2e2f33"/>
      </linearGradient>
    </defs>
    <polygon points="0,655 600,730 1200,655 1200,665 600,742 0,665" fill="#f7941d"/>
    <polygon points="0,0 1200,0 1200,630 600,715 0,630" fill="url(#workFill)"/>
  </svg>
  <h2 class="abs section-title light" style="top:2784px"><span class="mark"></span><span><span class="accent">What</span> Have We Done</span></h2>

  <div class="abs arrow-btn" style="left:0"><svg width="16" height="20" viewBox="0 0 16 20"><path d="M12 2 L4 10 L12 18" stroke="#fff" stroke-width="3" fill="none"/></svg></div>
  <div class="abs arrow-btn" style="left:1146px"><svg width="16" height="20" viewBox="0 0 16 20"><path d="M4 2 L12 10 L4 18" stroke="#fff" stroke-width="3" fill="none"/></svg></div>

  <article class="abs work-card" style="left:91px"><h3><span class="seal"></span>Northfield Assembly</h3><p>Lorem ipsum dolor sit amet, consectetur adipiscing elit, sed do eiusmod tempor incidi dunt ut labore et dolore magna aliqua. Lut enim ad minim veni am, quis nostrud exercitation ullamco laboris nisi ut aliquip.</p></article>
  <article class="abs work-card" style="left:443px"><h3>Coastal State Legislature</h3><p>Lorem ipsum dolor sit amet, consectetur adipiscing elit, sed do eiusmod tempor incidi dunt ut labore et dolore magna aliqua. Lut enim ad minim veni am, quis nostrud exercitation ullamco laboris nisi ut aliquip.</p></article>
  <article class="abs work-card" style="left:796px"><h3>Bureau of Civic Affairs</h3><p>Lorem ipsum dolor sit amet, consectetur adipiscing elit, sed do eiusmod tempor incidi dunt ut labore et dolore magna aliqua. Lut enim ad minim veni am, quis nostrud exercitation ullamco laboris nisi ut aliquip.</p></article>
</section>

<h2 class="abs section-title" style="top:3508px"><span class="mark"></span><span>How Can We Help</span></h2>
<form>
  <div class="abs field" style="left:116px;top:3606px;width:311px">Your Name</div>
  <div class="abs field" style="left:443px;top:3606px;width:311px">Your Email</div>
  <div class="abs field" style="left:770px;top:3606px;width:313px">Your Subject</div>
  <div class="abs field" style="left:116px;top:3664px;width:967px;height:130px">Message</div>
  <div class="abs btn-solid">Send</div>
</form>

<div class="abs map-area" role="img" aria-label="Street map showing the office location with a red pin"></div>

<footer>
  <svg class="abs footer-bg" width="1200" height="630" viewBox="0 0 1200 630">
    <polygon points="0,0 600,118 1200,0 1200,14 600,132 0,14" fill="#f7941d"/>
    <polygon points="0,14 600,132 1200,14 1200,630 0,630" fill="#3a3a3c"/>
  </svg>
  <div class="abs footer-brand"><span class="brand-dot"></span>Tallbridge</div>

  <div class="abs footer-col" style="left:178px">
    <h4>QUICK LINKS</h4>
    <ul><li><span class="tri"></span>Who Are We</li><li><span class="tri"></span>What Can We Do</li><li><span class="tri"></span>What Have We Done</li><li><span class="tri"></span>How Can We Help</li></ul>
  </div>
  <div class="abs footer-col" style="left:453px">
    <h4>CONTACT</h4>
    <ul>
      <li style="align-items:flex-start"><span class="icon-ring"></span><span>Tallbridge<br>Unit 3, 48 Kestrel Rd<br>Marlow, SA 5099</span></li>
      <li style="margin-top:10px"><span class="icon-ring"></span>1300 555 014</li>
      <li style="margin-top:10px"><span class="icon-ring"></span>info@tallbridge.com.au</li>
    </ul>
  </div>
  <div class="abs footer-col newsletter" style="left:770px">
    <h4 style="width:260px">NEWSLETTER SUBSCRIPTION</h4>
    <p>Register your email address to get more information about us</p>
    <div class="email-field">Email Address</div>
    <div class="subscribe">SUBSCRIBE</div>
  </div>

  <div class="abs bottom-bar"><span>COPYRIGHT © 2018 TALLBRIDGE. ALL RIGHTS RESERVED</span><div class="socials"><span></span><span></span><span></span><span></span><span></span></div></div>
</footer>

</body>
</html>
```